RTV Electrical – Fridge Magnet & Letterbox Leaflet

Overview
We are a local electrical contractor based in Gooseberry Hill in the Perth Hills (Western Australia).
We are looking for a designer to create:
1️⃣ A fridge magnet design
2️⃣ A matching letterbox leaflet (A6 or DL)
The goal is to create clean, professional marketing that feels local and trustworthy, not flashy advertising.
The designs must feel like a high-quality local trades business, appealing to homeowners in suburbs such as:
Kalamunda
Gooseberry Hill
Lesmurdie
Walliston
Pickering Brook
Design Style
The design should feel:
✔ Local
✔ Authentic
✔ Professional
✔ Trustworthy
✔ Clean and simple
NOT:
✖ Cheap advertising
✖ Overly flashy
✖ Busy or cluttered
Think premium local tradesman, not mass marketing.
Branding
Use our brand colours inspired by our van:
Primary colours
Navy Blue
White
Accent colour
Yellow / gold highlight
Design should match the look of our work van branding.
Images Provided
We will provide:
✔ Company logo
✔ Photo of our branded van in the Perth Hills
The van photo should be used in the leaflet design to reinforce our local presence.
Fridge Magnet Design
Size suggestion:
90mm x 55mm
Purpose:
Homeowners keep this magnet so they can easily call a trusted electrician.
Must include:
RTV Electrical Contracting
Local Perth Hills Electrician
Based in Gooseberry Hill
Phone number (large and clear)
📞 0491 726 054
Services:
• Fault finding
• Switchboard upgrades
• Lighting & power
• Ceiling fans
• Smoke alarm compliance
Also include:
⭐ 110+ Starfold Reviews
Website:
www.rtvelectrical.com.au
Design should be very simple and easy to read from across a kitchen.
Leaflet Design
Size options:
A6 or DL
Purpose:
Letterbox drop marketing in Perth Hills suburbs.
Front Side
Headline:
WE'RE WORKING IN YOUR AREA
Subtext:
Local electrician based in Gooseberry Hill
Include:
✔ Photo of our van
✔ RTV logo
✔ Key services
Services:
• Fault finding
• Switchboard upgrades
• Lighting & power
• Ceiling fans
• Smoke alarm compliance
Call to action:
📞 Call Marcus – 0491 726 054
⭐ 110+ Five-Star Starfold Reviews
Back Side
Headline:
Your Local Perth Hills Electrician
Servicing:
Kalamunda
Gooseberry Hill
Lesmurdie
Walliston
Pickering Brook
Short message:
Reliable electrical work across the Perth Hills.
Call Marcus
📞 0491 726 054
Website:
www.rtvelectrical.com.au
EC47286
Target Audience
Homeowners in the Perth Hills aged 35–70.
Many homes are older properties and often need electrical upgrades, repairs and safety work.
Design should appeal to homeowners who value reliability and local service.
Deliverables
Designers must provide:
✔ Print-ready files
✔ Editable source files
✔ High resolution files
For:
Fridge magnet
Leaflet front and back
Final Notes
This design should communicate:
✔ Trusted local electrician
✔ Established business
✔ Professional service
✔ Easy to contact
The goal is to create marketing people will keep, not throw away.

```html
<!DOCTYPE html>
<html lang="en">
<head>
<meta charset="utf-8">
<title>RTV Electrical – Fridge Magnet</title>
<link rel="stylesheet" href="https://fonts.googleapis.com/css2?family=Oswald:wght@300;400;500;600;700&family=Poppins:wght@300;400;500&display=swap">
<style>
  :root {
    --navy: #1d2654;
    --white: #ffffff;
    --gold: #c9a227;
    --gold-light: #f1e24a;
    --gold-dark: #b8902a;
    --charcoal: #3a3a3a;
    --ink: #222222;
    --grey-rule: #c8c8c8;
    --page: #efefef;
  }
  * { margin: 0; padding: 0; box-sizing: border-box; }
  html, body { width: 732px; height: 1200px; overflow: hidden; background: var(--page); }
  .stage { position: relative; width: 732px; height: 1200px; }
  .magnet {
    position: absolute; left: 16px; top: 386px;
    width: 1503px; height: 920px;
    transform: scale(0.4657); transform-origin: 0 0;
    background: var(--white); overflow: hidden;
    box-shadow: 0 6px 24px rgba(0,0,0,.18);
  }
  .abs { position: absolute; white-space: nowrap; }
  .shapes { left: 0; top: 0; }

  .brand { left: 85px; top: 85px; display: flex; align-items: center; gap: 32px; }
  .brand-mark { width: 105px; height: 155px; background: var(--navy); border-radius: 6px; }
  .brand-name { font-family: "Poppins", sans-serif; font-weight: 400; color: var(--navy); font-size: 38px; line-height: 50px; }
  .brand-name span { display: block; border-bottom: 2px solid var(--navy); padding-right: 12px; }

  .services-title { left: 860px; top: 78px; font-family: "Oswald", sans-serif; font-weight: 500; font-size: 86px; color: var(--gold); line-height: 1; letter-spacing: -1px; }
  .services { left: 858px; top: 185px; list-style: none; }
  .services li { font-family: "Poppins", sans-serif; font-size: 40px; color: var(--white); line-height: 50px; display: flex; align-items: center; gap: 16px; }
  .services svg { width: 22px; height: 22px; flex: none; }

  .headline { font-family: "Oswald", sans-serif; line-height: 1; }
  .headline-light { left: 82px; font-weight: 400; color: var(--charcoal); font-size: 110px; letter-spacing: -3px; }
  .headline-local { top: 335px; }
  .headline-hills { top: 430px; }
  .headline-strong { left: 80px; top: 520px; font-weight: 700; color: var(--navy); font-size: 140px; letter-spacing: -6px; }

  .base-bar { left: 0; top: 670px; width: 765px; height: 90px;
    background: linear-gradient(90deg, var(--gold-dark), var(--gold) 45%, var(--gold-light));
    display: flex; align-items: center; padding-left: 84px; gap: 14px; }
  .base-bar svg { width: 48px; height: 68px; flex: none; }
  .base-bar p { font-family: "Oswald", sans-serif; font-weight: 400; font-size: 60px; line-height: 1; color: var(--ink); letter-spacing: -1.5px; white-space: nowrap; }

  .rating { left: 898px; top: 512px; display: flex; align-items: center; }
  .rating-source { text-align: center; width: 210px; }
  .rating-source .name { font-family: "Poppins", sans-serif; font-weight: 400; font-size: 50px; color: var(--navy); line-height: 1; }
  .rating-source .stars { color: var(--gold); font-size: 28px; letter-spacing: 3px; margin-top: 6px; line-height: 1; }
  .rating-divider { width: 2px; height: 100px; background: var(--grey-rule); margin: 0 24px; }
  .rating-count { font-family: "Oswald", sans-serif; line-height: 1; }
  .rating-count .num { display: block; font-weight: 700; font-size: 70px; color: var(--navy); letter-spacing: -2px; }
  .rating-count .label { display: block; font-weight: 600; font-size: 30px; color: var(--gold); margin-top: 2px; }

  .phone { left: 805px; top: 645px; width: 612px; height: 115px; border-top: 3px solid var(--navy); border-bottom: 3px solid var(--navy); display: flex; align-items: center; gap: 14px; padding-left: 7px; }
  .phone svg { width: 82px; height: 82px; flex: none; }
  .phone p { font-family: "Oswald", sans-serif; font-weight: 700; font-size: 94px; color: var(--gold); letter-spacing: -2px; line-height: 1; white-space: nowrap; }

  .web-band { left: 0; top: 785px; width: 1503px; height: 135px; background: var(--navy); display: flex; align-items: center; justify-content: center; }
  .web-band p { font-family: "Poppins", sans-serif; font-weight: 400; font-size: 54px; letter-spacing: 3px; color: var(--white); }
</style>
</head>
<body>
<div class="stage">
  <div class="magnet">
    <svg class="abs shapes" width="1503" height="920" viewBox="0 0 1503 920" aria-hidden="true">
      <polygon points="600,0 1503,0 1503,470 740,470" fill="var(--navy)"/>
      <rect x="530" y="70" width="290" height="350" rx="40" fill="var(--navy)" stroke="var(--white)" stroke-width="18" transform="rotate(12 675 245)"/>
    </svg>

    <div class="abs brand">
      <div class="brand-mark"></div>
      <div class="brand-name"><span>RTV Electrical</span><span>Contracting</span></div>
    </div>

    <h2 class="abs services-title">Our Services</h2>
    <ul class="abs services">
      <li><svg viewBox="0 0 22 22"><circle cx="11" cy="11" r="9.5" fill="none" stroke="#fff" stroke-width="1.6"/><path d="M6.5 11.2l3 3 6-6.2" fill="none" stroke="#fff" stroke-width="1.8"/></svg>FAULT FINDING</li>
      <li><svg viewBox="0 0 22 22"><circle cx="11" cy="11" r="9.5" fill="none" stroke="#fff" stroke-width="1.6"/><path d="M6.5 11.2l3 3 6-6.2" fill="none" stroke="#fff" stroke-width="1.8"/></svg>SWITCHBOARD UPGRADES</li>
      <li><svg viewBox="0 0 22 22"><circle cx="11" cy="11" r="9.5" fill="none" stroke="#fff" stroke-width="1.6"/><path d="M6.5 11.2l3 3 6-6.2" fill="none" stroke="#fff" stroke-width="1.8"/></svg>LIGHTING &amp; POWER</li>
      <li><svg viewBox="0 0 22 22"><circle cx="11" cy="11" r="9.5" fill="none" stroke="#fff" stroke-width="1.6"/><path d="M6.5 11.2l3 3 6-6.2" fill="none" stroke="#fff" stroke-width="1.8"/></svg>CEILING FANS</li>
      <li><svg viewBox="0 0 22 22"><circle cx="11" cy="11" r="9.5" fill="none" stroke="#fff" stroke-width="1.6"/><path d="M6.5 11.2l3 3 6-6.2" fill="none" stroke="#fff" stroke-width="1.8"/></svg>SMOKE ALARM COMPLIANCE</li>
    </ul>

    <h1 class="headline">
      <span class="abs headline-light headline-local">LOCAL</span>
      <span class="abs headline-light headline-hills">PERTH HILLS</span>
      <span class="abs headline-strong">ELECTRICIAN</span>
    </h1>

    <div class="abs base-bar">
      <svg viewBox="0 0 50 70" aria-hidden="true"><path d="M25 2C12 2 3 11 3 24c0 16 22 43 22 43s22-27 22-43C47 11 38 2 25 2z" fill="var(--ink)"/><circle cx="25" cy="23" r="8" fill="var(--gold)"/></svg>
      <p>BASED IN GOOSEBERRY HILL</p>
    </div>

    <div class="abs rating">
      <div class="rating-source">
        <div class="name">Starfold</div>
        <div class="stars">★★★★★</div>
      </div>
      <div class="rating-divider"></div>
      <div class="rating-count"><span class="num">110+</span><span class="label">REVIEWS</span></div>
    </div>

    <div class="abs phone">
      <svg viewBox="0 0 82 82" aria-hidden="true">
        <circle cx="41" cy="41" r="40" fill="var(--navy)"/>
        <path d="M27 22c2-2 4-2 5 0l5 8c1 2 0 3-1 4l-3 3c2 5 6 9 11 11l3-3c1-1 2-2 4-1l8 5c2 1 2 3 0 5l-3 4c-3 3-9 2-17-4-8-6-14-14-15-21 0-4 1-8 3-11z" fill="var(--gold)"/>
        <path d="M48 24a12 12 0 0 1 10 10M48 16a20 20 0 0 1 18 18" fill="none" stroke="var(--gold)" stroke-width="3.5" stroke-linecap="round"/>
      </svg>
      <p>0491 726 054</p>
    </div>

    <div class="abs web-band"><p>www.rtvelectrical.com.au</p></div>
  </div>
</div>
</body>
</html>
```